Training in Brief Tobacco Use Interventions

We need a design/template for an e-learning course. The course is being created for healthcare professionals. The template should include a home page (title), and subtitle page (introduction, chapter, test, help, references and so on). We would like to see designs that are very professional and appealling.

Reason: Can you extend deadline. I have not heard back from designers.

Target Market(s)

Healthcare professionals

Industry/Entity Type

Health Care

Number of Pages Required

4 page

Font styles to use
Sans Serif

Colors
3276b5
85acd3
ffc214
f37122
ffcf3e
886aae
acd136

Requirements
Must have
• The project's title page should be very professional and appealing for a very serious audience. The title page should include an image of healthcare provider, and/or no smoking symbol.
Nice to have
• Pages should include icons such as next and previous buttons, along with progress status bar on bottom of design. Also should include top row containing for primary chapters. In addition, left side of page should contain space for detailed table of contents and additional resources.
Should not have
• Design should not appear cluttered or confusing. Large space for logo.

```html
<!DOCTYPE html>
<html lang="en">
<head>
<meta charset="utf-8">
<title>Smokefree Practice Academy – Learning Course</title>
<link rel="stylesheet" href="https://fonts.googleapis.com/css2?family=Lato:wght@400;700&family=Fjalla+One&family=Bitter:wght@700&display=swap">
<style>
:root{
  --orange:#f37122;
  --blue:#3a76b4;
  --navy:#0f1a26;
  --green:#acd136;
  --green-dark:#7f9f22;
  --footer:#2f2f2f;
  --white:#ffffff;
  --ink:#1b2430;
}
*{box-sizing:border-box;margin:0;padding:0}
html,body{width:1200px;height:726px;overflow:hidden}
body{position:relative;font-family:"Lato",sans-serif;background:var(--blue);color:var(--white)}
.top-nav{position:absolute;left:0;top:0;width:1200px;height:41px;background:var(--orange)}
.top-nav ul{list-style:none;display:flex;margin-left:161px;height:100%;align-items:center}
.top-nav li{font-size:13px;text-transform:uppercase;padding:0 19px;border-left:1px solid rgba(0,0,0,.12);line-height:26px}
.top-nav li.is-active{color:var(--ink)}
.nav-phone{position:absolute;left:903px;top:0;height:41px;border-left:1px solid rgba(0,0,0,.12);display:flex;align-items:center;gap:8px;padding-left:20px;font-weight:700;font-size:13px}
.backdrop{position:absolute;left:0;top:41px;width:1200px;height:586px;
  background:
    radial-gradient(ellipse 220px 260px at 1130px 300px,rgba(30,70,120,.35),transparent 70%),
    radial-gradient(ellipse 260px 200px at 760px 520px,rgba(120,160,205,.35),transparent 70%),
    linear-gradient(90deg,#6f98c8 0%,#4b80bb 14%,var(--blue) 40%,#4780bb 70%,#3a76b4 100%)}
.figure-left{position:absolute;left:38px;top:120px;width:123px;height:507px;
  background:linear-gradient(180deg,rgba(235,242,249,.6) 0%,rgba(200,220,240,.55) 45%,rgba(120,155,195,.5) 100%);border-radius:50px 50px 0 0}
.sidebar{position:absolute;left:161px;top:41px;width:240px;height:586px;background:var(--navy)}
.brand{position:absolute;left:0;top:68px;width:240px;text-align:center;font-family:"Fjalla One",sans-serif;font-size:27px;line-height:36px;color:var(--green);letter-spacing:.5px}
.brand-dot{display:inline-block;width:12px;height:12px;border-radius:50%;background:var(--green);margin-right:6px;vertical-align:middle}
.course-title{position:absolute;left:14px;top:207px;font-weight:700;font-size:15.5px}
.course-list{position:absolute;left:13px;top:237px;width:215px;list-style:none;border:1px solid rgba(255,255,255,.25)}
.course-list li{font-size:11px;height:37.5px;display:flex;align-items:center;padding-left:10px;border-top:1px solid rgba(255,255,255,.18)}
.course-list li:first-child{border-top:0;height:33px}
.course-list li::before{content:"›";margin-right:9px;font-size:13px}
.hero{position:absolute;left:418px;top:59px;width:619px;height:363px;border:3px solid #e9f0f7;box-shadow:0 0 0 2px rgba(40,90,150,.6);overflow:hidden}
.hero-photo{position:absolute;inset:0;
  background:
    radial-gradient(ellipse 150px 260px at 470px 250px,rgba(255,255,255,.95),transparent 70%),
    radial-gradient(ellipse 90px 150px at 470px 230px,rgba(90,140,200,.45),transparent 70%),
    radial-gradient(ellipse 120px 200px at 230px 190px,rgba(150,200,230,.7),transparent 70%),
    radial-gradient(ellipse 90px 170px at 60px 230px,rgba(120,175,215,.6),transparent 70%),
    radial-gradient(ellipse 160px 80px at 190px 300px,rgba(245,245,240,.9),transparent 70%),
    linear-gradient(100deg,#e6eef4 0%,#d7e5ef 40%,#eef2f5 65%,#f6f7f8 100%)}
.hero-title{position:absolute;left:23px;top:276px;font-family:"Fjalla One",sans-serif;font-size:23px;color:var(--ink)}
.hero-sub{position:absolute;left:23px;top:318px;font-family:"Bitter",serif;font-weight:700;font-size:15px;color:var(--ink)}
.no-smoke{position:absolute;left:521px;top:276px}
.about{position:absolute;left:424px;top:450px;width:616px}
.about h1{font-size:25.5px;font-weight:700}
.about p{margin-top:12px;font-size:11.8px;line-height:18px;color:#eef3f9}
.progress-band{position:absolute;left:0;top:627px;width:1200px;height:45px;background:var(--green)}
.progress-track{position:absolute;left:163px;top:14px;width:265px;height:17px;border-radius:9px;background:var(--white);border:3px solid var(--green-dark)}
.progress-fill{position:absolute;left:2px;top:2px;width:86px;height:7px;border-radius:4px;background:#283038}
.progress-count{position:absolute;left:434px;top:14px;font-weight:700;font-size:14px;color:#2a3440}
.pager{position:absolute;top:11px;width:27px;height:25px;background:var(--green-dark);display:flex;align-items:center;justify-content:center}
.pager-prev{left:972px}.pager-next{left:1009px}
.site-footer{position:absolute;left:0;top:672px;width:1200px;height:54px;background:var(--footer)}
.copyright{position:absolute;left:161px;top:20px;font-size:12.5px;font-weight:700}
.social{position:absolute;left:893px;top:11px;display:flex;gap:6px}
.social span{width:32px;height:32px;border-radius:50%;border:2px solid #e6e6e6;display:flex;align-items:center;justify-content:center}
</style>
</head>
<body>
<nav class="top-nav">
  <ul>
    <li class="is-active">Home</li><li>Introduction</li><li>Chapter</li><li>Test</li><li>About Us</li><li>Courses</li><li>Contact Us</li>
  </ul>
  <div class="nav-phone">
    <svg width="18" height="18" viewBox="0 0 24 24" fill="none" stroke="#fff" stroke-width="1.6"><path d="M5 3h4l2 5-3 2a12 12 0 0 0 6 6l2-3 5 2v4a2 2 0 0 1-2 2A18 18 0 0 1 3 5a2 2 0 0 1 2-2z"/></svg>
    (55) 010 234 5678
  </div>
</nav>

<div class="backdrop" role="img" aria-label="Soft blue clinical background with medical staff"></div>
<div class="figure-left" role="img" aria-label="Faded photo of a senior doctor in a white coat"></div>

<aside class="sidebar">
  <div class="brand"><span class="brand-dot"></span>SMOKEFREE PRACTICE<br>ACADEMY</div>
  <h2 class="course-title">LEARNING COURSE.</h2>
  <ul class="course-list">
    <li>Adolescent Health</li><li>Advanced Radiotherapy</li><li>Audiology</li><li>Electronic Fetal Monitoring</li><li>Adolescent Health</li><li>Foundation Programme</li><li>Female Genital Mutilation</li>
  </ul>
</aside>

<section class="hero">
  <div class="hero-photo" role="img" aria-label="Photo of a smiling female doctor with a clipboard and a nurse caring for a patient"></div>
  <div class="hero-title">Brief Clinical InterventionsFor Tobacco Use</div>
  <div class="hero-sub">Tips for Busy Healthcare Providers</div>
  <svg class="no-smoke" width="76" height="76" viewBox="0 0 76 76" aria-label="No smoking">
    <circle cx="38" cy="38" r="33" fill="#fff" stroke="#d81f26" stroke-width="7"/>
    <rect x="16" y="42" width="36" height="8" fill="#111"/><rect x="54" y="42" width="5" height="8" fill="#111"/>
    <path d="M50 38c0-6 6-6 6-12s-5-6-5-10" fill="none" stroke="#111" stroke-width="2.5"/>
    <line x1="15" y1="15" x2="61" y2="61" stroke="#d81f26" stroke-width="7"/>
  </svg>
</section>

<section class="about">
  <h1>About Smokefree Practice Academy</h1>
  <p>Lorem ipsum dolor sit amet, consectetur adipiscing elit, sed do eiusmod tempor incididunt ut labore et dolore magna aliqua. Ut enim ad minim veniam, quis nostrud exercitation ullamco laboris nisi ut aliquip ex ea commodo consequat. Duis aute irure dolor in reprehenderit in voluptate velit esse cillum dolore eu fugiat nulla pariatur. Excepteur sint occaecat cupidatat non proident, sunt in culpa qui officia deserunt mollit anim id est laborum {..}</p>
</section>

<div class="progress-band">
  <div class="progress-track"><div class="progress-fill"></div></div>
  <div class="progress-count">1/8</div>
  <div class="pager pager-prev"><svg width="12" height="14" viewBox="0 0 12 14"><path d="M10 1 2 7l8 6z" fill="none" stroke="#fff" stroke-width="1.5"/></svg></div>
  <div class="pager pager-next"><svg width="12" height="14" viewBox="0 0 12 14"><path d="M2 1l8 6-8 6z" fill="none" stroke="#fff" stroke-width="1.5"/></svg></div>
</div>

<footer class="site-footer">
  <div class="copyright">© 2016 Smokefree Practice Academy . All Rights Reserved.</div>
  <div class="social">
    <span aria-label="Share"><svg width="14" height="14" viewBox="0 0 14 14" fill="#fff"><circle cx="3" cy="7" r="2"/><circle cx="11" cy="3" r="2"/><circle cx="11" cy="11" r="2"/><path d="M3 7 11 3M3 7l8 4" stroke="#fff" stroke-width="1.2"/></svg></span>
    <span aria-label="Email"><svg width="14" height="12" viewBox="0 0 14 12" fill="none" stroke="#fff" stroke-width="1.4"><rect x="1" y="1" width="12" height="10"/><path d="M1 1l6 5 6-5"/></svg></span>
    <span aria-label="Website"><svg width="14" height="14" viewBox="0 0 14 14" fill="none" stroke="#fff" stroke-width="1.3"><circle cx="7" cy="7" r="6"/><path d="M1 7h12M7 1c3 3 3 9 0 12M7 1c-3 3-3 9 0 12"/></svg></span>
    <span aria-label="Messages"><svg width="14" height="13" viewBox="0 0 14 13" fill="none" stroke="#fff" stroke-width="1.4"><path d="M1 1h12v8H6l-3 3V9H1z"/></svg></span>
  </div>
</footer>
</body>
</html>
```